Fully self produced folk band seeking cd cover for their first EP !

Hi ! We are TinLanterns : a folk trio from the Swiss alps. We are a fully amateur band : we play music and write songs during our free time, and we record our songs in our living room. These last few years, we have been very active at playing intimate shows in Switzerland : in flats, winemaker vaults, balconies... In 2015 we are compiling some of our original songs in our first EP, that could help us get us to the next level, and maybe encourage us to spend more time doing music, or afford some time in a real studio. You can listen to us : https://tunehollow.example/tinlanterns
https://www.clipwaves.example/watch?v=9Qk2Rm7Ls1x

Today we are looking for a cd cover for our EP. It will be a standard 12x12 simple cardboard jacket. The title of our EP is "A corner of meadow kept for tomorrow". We would like the title to appear on the cover. We would like the background to be "beige / brown" (like old paper), with shapes using very few colours. We attached some other covers that inspire us. We are also attaching our logo, which can also appear on the cover.

Just in case, here is the order of the songs on our EP :
Copper hill story
Steady
Oh Sparrow
Kings and lanterns
Nightfall

Good luck !

Target Market(s)

Music lovers

Industry/Entity Type

Movie

Font styles to use
Sans Serif
Decorative

Requirements
Must have
• Our Logo
• Our Title
• A connection to our music
Nice to have
• A design that we could easily adapt for the print on the cd and the back of the jacket.
• A typeface that we can reuse.

```html
<!DOCTYPE html>
<html lang="en">
<head>
<meta charset="utf-8">
<title>TinLanterns – A corner of meadow kept for tomorrow</title>
<link rel="stylesheet" href="https://fonts.googleapis.com/css2?family=Almendra:ital@1&family=Amatic+SC:wght@700&display=swap">
<style>
  :root {
    --page: #ffffff;
    --paper: #e6d4b8;
    --paper-light: #eddfc8;
    --paper-dark: #d7c09d;
    --ink: #4a2a14;
    --ink-soft: #6b4428;
    --ink-faint: rgba(90, 55, 25, .35);
    --board: #7a5233;
    --board-text: #ead9bd;
    --tape: #c9c58e;
    --tape-edge: #e3d49a;
    --tape-pink: #d9a59a;
    --burn: #7a1f22;
    --wood: #6b3b1c;
    --hub: #cfcac2;
  }
  * { box-sizing: border-box; margin: 0; padding: 0; }
  html, body { width: 1200px; height: 508px; overflow: hidden; background: var(--page); }
  .canvas { position: relative; width: 1200px; height: 508px; }

  .jacket {
    position: absolute; left: 43px; top: 43px; width: 770px; height: 386px;
    background: linear-gradient(135deg, var(--paper-light), var(--paper) 55%, var(--paper-dark));
    overflow: hidden;
  }
  .panel { position: absolute; top: 0; height: 100%; }
  .panel--back { left: 0; width: 384px; border-right: 1px solid var(--ink-faint); }
  .panel--front { left: 384px; width: 386px; }

  .ornament { position: absolute; border-radius: 40%; background: radial-gradient(ellipse, rgba(110,70,40,.35), rgba(110,70,40,0) 70%); }
  .ornament--top { left: 60px; top: 14px; width: 250px; height: 44px; }
  .ornament--bottom { left: 80px; top: 96px; width: 220px; height: 40px; }
  .ornament--end { left: 160px; top: 330px; width: 44px; height: 24px; }

  .header-rule { position: absolute; left: 0; top: 87px; width: 384px; height: 2px; background: var(--ink-soft); }
  .header-name {
    position: absolute; top: 58px; left: 50%; transform: translateX(-50%);
    padding: 0 12px; background: var(--paper); white-space: nowrap;
    font: 700 40px/1 "Amatic SC", sans-serif; letter-spacing: 6px; color: var(--ink);
  }

  .tracklist { position: absolute; left: 100px; top: 134px; list-style: none; }
  .tracklist li { font: italic 24px/36px "Almendra", serif; color: var(--ink); white-space: nowrap; }
  .closing-rule { position: absolute; left: 65px; top: 322px; width: 262px; height: 2px; background: var(--ink-soft); }
  .closing-rule::before, .closing-rule::after { content: ""; position: absolute; top: -2px; width: 6px; height: 6px; border-radius: 50%; background: var(--ink-soft); }
  .closing-rule::before { left: -4px; } .closing-rule::after { right: -4px; }

  .stain-band { position: absolute; left: 275px; top: 315px; width: 160px; height: 60px; background: rgba(140, 95, 50, .25); transform: rotate(-40deg); }

  .ironwork { position: absolute; left: 15px; top: 11px; width: 210px; height: 240px; border-radius: 12px; background: radial-gradient(ellipse at 40% 45%, rgba(110,74,44,.45), rgba(110,74,44,.08) 75%); }
  .sign-board {
    position: absolute; left: 24px; top: 128px; width: 171px; height: 56px;
    background: var(--board); border-radius: 4px;
    display: flex; align-items: center; justify-content: center;
    font: 700 34px/1 "Amatic SC", sans-serif; letter-spacing: 3px; color: var(--board-text);
  }
  .burnt-corner { position: absolute; right: 0; top: 0; width: 170px; height: 58px; border-bottom-left-radius: 70px 50px; background: linear-gradient(200deg, var(--wood), var(--burn) 80%); }

  .title-tape {
    position: absolute; left: 100px; top: 245px; width: 262px; height: 48px;
    background: var(--tape); border-bottom: 3px solid var(--tape-pink);
    transform: rotate(-3deg); text-align: center;
    font: 700 22px/20px "Amatic SC", sans-serif; letter-spacing: 1px; color: var(--ink); padding-top: 4px;
  }
  .title-tape::before, .title-tape::after { content: ""; position: absolute; top: -8px; width: 30px; height: 18px; background: var(--tape-edge); opacity: .85; }
  .title-tape::before { left: -14px; transform: rotate(-30deg); }
  .title-tape::after { right: -14px; transform: rotate(-30deg); }

  .ground-line { position: absolute; left: 0; height: 2px; width: 400px; background: var(--ink-soft); opacity: .7; transform-origin: left; transform: rotate(-2.5deg); }
  .ground-line--1 { top: 330px; } .ground-line--2 { top: 350px; }

  .disc { position: absolute; left: 811px; top: 77px; width: 318px; height: 318px; }
  .disc-name { font: 700 34px "Amatic SC", sans-serif; letter-spacing: 3px; fill: var(--board-text); }
  .disc-title { font: 700 20px "Amatic SC", sans-serif; letter-spacing: 1px; fill: var(--ink); }
</style>
</head>
<body>
<main class="canvas">
  <section class="jacket" aria-label="EP jacket">
    <div class="panel panel--back">
      <div class="ornament ornament--top" role="img" aria-label="Scrolling flourish above the band name"></div>
      <div class="header-rule"></div>
      <h1 class="header-name">TinLanterns</h1>
      <div class="ornament ornament--bottom" role="img" aria-label="Scrolling flourish below the band name"></div>
      <ol class="tracklist">
        <li>Copper hill story</li>
        <li>Steady</li>
        <li>Oh Sparrow</li>
        <li>Kings and lanterns</li>
        <li>Nightfall</li>
      </ol>
      <div class="closing-rule"></div>
      <div class="ornament ornament--end" role="img" aria-label="Small ornament closing the track list"></div>
      <div class="stain-band" role="img" aria-label="Faded paper stain"></div>
    </div>
    <div class="panel panel--front">
      <div class="burnt-corner" role="img" aria-label="Burnt paper corner revealing wood"></div>
      <div class="ironwork" role="img" aria-label="Wrought iron shop sign bracket"></div>
      <div class="sign-board">TinLanterns</div>
      <div class="ground-line ground-line--1"></div>
      <div class="ground-line ground-line--2"></div>
      <h2 class="title-tape">A corner of meadow<br>kept for tomorrow</h2>
    </div>
  </section>

  <svg class="disc" viewBox="0 0 322 322" aria-label="CD print">
    <defs>
      <linearGradient id="disc-paper" x1="0" y1="0" x2="1" y2="1">
        <stop offset="0" stop-color="var(--paper-light)"/>
        <stop offset="1" stop-color="var(--paper-dark)"/>
      </linearGradient>
      <clipPath id="disc-clip"><circle cx="161" cy="161" r="161"/></clipPath>
    </defs>
    <g clip-path="url(#disc-clip)">
      <circle cx="161" cy="161" r="161" fill="url(#disc-paper)"/>
      <path d="M300 40 Q330 120 322 200 L322 0 Z" fill="var(--burn)"/>
      <g transform="rotate(30 161 161)">
        <rect x="40" y="-40" width="220" height="160" rx="12" fill="rgba(110,74,44,.18)" role="img" aria-label="Wrought iron shop sign bracket"/>
        <rect x="62" y="36" width="170" height="54" rx="4" fill="var(--board)"/>
        <text class="disc-name" x="147" y="75" text-anchor="middle">TinLanterns</text>
      </g>
      <circle cx="161" cy="161" r="66" fill="var(--hub)" opacity=".85"/>
      <circle cx="161" cy="161" r="24" fill="var(--page)"/>
      <g transform="rotate(30 161 161)">
        <rect x="-10" y="292" width="360" height="2" fill="var(--ink-soft)" opacity=".7"/>
        <rect x="-10" y="310" width="360" height="2" fill="var(--ink-soft)" opacity=".7"/>
        <rect x="36" y="236" width="250" height="46" fill="var(--tape)"/>
        <rect x="36" y="280" width="250" height="3" fill="var(--tape-pink)"/>
        <text class="disc-title" x="161" y="256" text-anchor="middle">A corner of meadow</text>
        <text class="disc-title" x="161" y="276" text-anchor="middle">kept for tomorrow</text>
      </g>
    </g>
  </svg>
</main>
</body>
</html>
```